Criminal Defense Law Firm needs Stationary design Theme for a Business Card, Envelope, and Letterhea

Our Law Firm is seeking a general design concept for a business card, letterhead, and Envelope.

Our website is QuillmoreAdvocates.com

A design for these three items is requested to keep branding in place for the firm. Would like to keep the Firm Colors on the website consistent with our branding on business cards, letterheads, and mailing envelopes #10 size to be exact.

We would like business cards printed front and back with Law firm Colors from website.

Letterhead with law firm colors as well. Design is not limited to just the header, but the footer can be utilized as well for email, website, phone, fax, etc.

Simple #10 envelope consisting of the same design principles set out in the previous two designs.

```html
<!DOCTYPE html>
<html lang="en">
<head>
<meta charset="utf-8">
<title>Quillmore Advocates – Business Card</title>
<link rel="stylesheet" href="https://fonts.googleapis.com/css2?family=Marcellus&family=Open+Sans:wght@400;600&display=swap">
<style>
  :root {
    --teal: #0ea8cc;
    --gold: #b39c6c;
    --ink: #1a1a1a;
    --paper: #ffffff;
    --rule: #cfcfcf;
    --text: #4a4a4a;
    --backdrop: #ebe7e0;
  }
  html, body {
    margin: 0;
    width: 1200px;
    height: 1024px;
    overflow: hidden;
    background: var(--backdrop);
  }
  .stage {
    position: relative;
    width: 1200px;
    height: 1024px;
  }
  .card {
    position: absolute;
    left: 250px;
    width: 700px;
    height: 400px;
    overflow: hidden;
    box-shadow: 0 6px 18px rgba(0,0,0,0.18);
  }
  .card-front { top: 90px; background: var(--paper); }
  .card-back { top: 540px; background: var(--teal); }
  .front-shapes { position: absolute; inset: 0; }
  .front-url {
    position: absolute;
    left: 36px;
    top: 42px;
    font: 400 17px "Open Sans", sans-serif;
    color: var(--paper);
    letter-spacing: 0.3px;
  }
  .brand {
    position: absolute;
    display: flex;
    align-items: center;
    gap: 16px;
  }
  .card-front .brand { left: 44px; top: 158px; }
  .brand-mark {
    width: 50px;
    height: 50px;
    border-radius: 50%;
    border: 2px solid var(--ink);
    box-sizing: border-box;
    flex: none;
  }
  .brand-name {
    font: 400 25px/1.05 "Marcellus", serif;
    text-transform: uppercase;
    letter-spacing: 1px;
    color: var(--ink);
  }
  .person {
    position: absolute;
    left: 44px;
    top: 234px;
    font: 600 18px "Open Sans", sans-serif;
    color: var(--gold);
  }
  .person .divider { color: var(--rule); font-weight: 400; margin: 0 6px; }
  .person .role { color: var(--teal); font-weight: 400; font-size: 16px; }
  .rule {
    position: absolute;
    left: 44px;
    right: 40px;
    height: 1px;
    background: var(--rule);
  }
  .rule-top { top: 272px; }
  .rule-bottom { top: 360px; }
  .contact {
    position: absolute;
    left: 44px;
    font: 400 15px "Open Sans", sans-serif;
    color: var(--text);
    display: flex;
    align-items: center;
    gap: 8px;
  }
  .contact-address { top: 284px; }
  .contact-lines { top: 318px; }
  .contact .email { color: var(--teal); }
  .icon {
    width: 16px;
    height: 16px;
    flex: none;
  }
  .card-back .brand { left: 150px; top: 130px; }
  .card-back .brand-mark { border-color: var(--paper); width: 58px; height: 58px; }
  .card-back .brand-name { color: var(--paper); font-size: 29px; }
  .back-url {
    position: absolute;
    left: 150px;
    top: 250px;
    font: 400 16px "Open Sans", sans-serif;
    color: var(--paper);
  }
</style>
</head>
<body>
<main class="stage">

  <section class="card card-front" aria-label="Business card front">
    <svg class="front-shapes" width="700" height="400" viewBox="0 0 700 400" aria-hidden="true">
      <path fill="var(--teal)" d="M0 0 H470 C400 22 330 88 250 100 C160 112 70 100 0 122 Z"/>
      <path fill="var(--gold)" d="M0 122 C70 100 160 112 250 100 C330 88 400 22 470 0 H515 C440 30 355 112 262 124 C170 136 80 126 0 148 Z"/>
      <path fill="var(--ink)" d="M545 0 C600 24 655 30 700 26 V0 Z"/>
      <path fill="var(--teal)" d="M600 0 C640 10 675 13 700 11 V0 Z"/>
    </svg>

    <div class="front-url">www.QuillmoreAdvocates.com</div>

    <div class="brand">
      <span class="brand-mark"></span>
      <div class="brand-name">Quillmore Advocates<br>Law Offices</div>
    </div>

    <div class="person">Daniel Harlow<span class="divider">|</span><span class="role">Lawyer</span></div>

    <div class="rule rule-top"></div>

    <div class="contact contact-address">2214 Cedar Lane SW, Fairhaven, NM 87150</div>

    <div class="contact contact-lines">
      <svg class="icon" viewBox="0 0 16 16" aria-hidden="true"><circle cx="8" cy="8" r="7" fill="var(--gold)" stroke="var(--teal)" stroke-width="1.5"/><path d="M5.5 4.5 l1.5 0 l0.7 2 l-1 0.8 a5 5 0 0 0 2 2 l0.8 -1 l2 0.7 l0 1.5 a1 1 0 0 1 -1 1 a7 7 0 0 1 -6 -6 a1 1 0 0 1 1 -1z" fill="#fff"/></svg>
      <span>555.310.4471</span>
      <svg class="icon" viewBox="0 0 16 16" aria-hidden="true"><circle cx="8" cy="8" r="7" fill="var(--gold)" stroke="var(--teal)" stroke-width="1.5"/><rect x="5" y="4" width="6" height="8" rx="1" fill="#fff"/></svg>
      <span>555.310.4472</span>
      <svg class="icon" viewBox="0 0 16 16" aria-hidden="true"><circle cx="8" cy="8" r="7" fill="var(--gold)" stroke="var(--teal)" stroke-width="1.5"/><rect x="4" y="5" width="8" height="6" fill="#fff"/><path d="M4 5 L8 8.5 L12 5" fill="none" stroke="var(--gold)" stroke-width="1"/></svg>
      <span class="email">name@QuillmoreAdvocates.com</span>
    </div>

    <div class="rule rule-bottom"></div>
  </section>

  <section class="card card-back" aria-label="Business card back">
    <div class="brand">
      <span class="brand-mark"></span>
      <div class="brand-name">Quillmore Advocates<br>Law Offices</div>
    </div>
    <div class="back-url">www.QuillmoreAdvocates.com</div>
  </section>

</main>
</body>
</html>
```